Technology solutions catalog

Were looking for a catalogue to supplement our website and corporate branding.

Our website will give you a good understanding of our products and services as well as our theme.

Our base colour and logo is red, white and grey.

www.voltrane.com.au

The aim of the catalogue is to showcase our business IT services & solutions. This will be a mix of education about the new solutions available to small and medium business today and how these solutions can increase productivity.

We would also like tip sections

This isn't all about selling but also about educating SMB's of the new and exciting IT solutions available today and having them book a free consult with us to discuss further about how we can help the business.

Solutions and area's that the catalogue will need to cover include

Front Cover -
-About us section, with our business contact information (1st page)
- Introduction. (2nd page)
-Communication Solutions - this includes Email, IP phones and business IT networks (2 pages)
- Data & Storage solutions (2 pages)
- Hardware (1 pages)
- Business IT health check list (1 page)
- Services and support offering (2 pages)
- Software & Popular cloud solutions (2 pages)
- Website / E-commerce solutions (2 pages)
Back cover

Based on two pages per solution the whole catalogue will be around 14 pages.

We don't need any text content done. We would like Headings on pages including page numbers. Footer please.

We're looking for a template that we can have our designer finish off by adding in some further product and service image and text.

Thank you for your consideration

Target Market(s)

IT for small and medium businesses

Industry/Entity Type

Supplement

Requirements
Must have
• Size A4
• Design supplied in Adobe indesign so we can edit and add our text and content
• Clean design

```html
<!DOCTYPE html>
<html lang="en">
<head>
<meta charset="utf-8">
<title>Voltrane Catalogue – Communications</title>
<link href="https://fonts.googleapis.com/css2?family=Arimo:ital,wght@0,400;0,700;1,400&family=Roboto:wght@300&display=swap" rel="stylesheet">
<style>
  :root {
    --brand-red: #c8202a;
    --ink: #231f20;
    --icon-disc: #ececec;
    --panel: #f4f4f4;
    --page: #ffffff;
    --gutter-shade: rgba(0,0,0,0.13);
  }
  * { margin: 0; padding: 0; box-sizing: border-box; }
  html, body { width: 1200px; height: 848px; overflow: hidden; background: var(--page); }
  body { font-family: "Arimo", Arial, sans-serif; color: var(--ink); position: relative; }

  .page { position: absolute; top: 0; height: 848px; background: var(--page); }
  .page--left { left: 0; width: 598px; }
  .page--right { left: 598px; width: 602px; }
  .page--right::before {
    content: ""; position: absolute; left: 0; top: 0; width: 46px; height: 100%;
    background: linear-gradient(to right, var(--gutter-shade), rgba(0,0,0,0));
  }
  .page--left::after {
    content: ""; position: absolute; right: 0; top: 0; width: 14px; height: 100%;
    background: linear-gradient(to left, rgba(0,0,0,0.05), rgba(0,0,0,0));
  }

  .section-label {
    position: absolute; left: 43px; top: 45px;
    font-weight: 700; font-size: 17px; color: var(--brand-red); letter-spacing: 0.2px;
  }
  .section-title {
    position: absolute; left: 42px; top: 78px; width: 400px;
    font-family: "Roboto", Arial, sans-serif; font-weight: 300;
    font-size: 29.5px; line-height: 31.5px; color: var(--brand-red);
  }

  .feature-icon {
    position: absolute; width: 80px; height: 80px; border-radius: 50%;
    background: var(--icon-disc); display: flex; align-items: center; justify-content: center;
  }
  .feature-icon svg { width: 24px; height: 24px; fill: var(--brand-red); }

  .feature { position: absolute; font-size: 12px; line-height: 16px; }
  .feature h2 { font-size: 12.5px; font-weight: 700; color: var(--brand-red); line-height: 15px; }
  .feature p { margin-bottom: 9px; }
  .feature ul { list-style: none; }
  .feature li { position: relative; padding-left: 20px; }
  .feature li::before {
    content: ""; position: absolute; left: 3px; top: 7px; width: 3px; height: 3px;
    border-radius: 50%; background: var(--brand-red);
  }
  .feature--spaced li { margin-bottom: 8px; }

  .app-panel {
    position: absolute; left: 175px; top: 658px; width: 357px; height: 143px;
    background: var(--panel); display: grid;
    grid-template-columns: repeat(3, 1fr); grid-template-rows: repeat(2, 1fr);
    align-items: center; justify-items: center; padding: 4px 0;
  }
  .app { display: flex; flex-direction: column; align-items: center; gap: 5px; font-size: 11px; color: var(--ink); }
  .app-mark { width: 34px; height: 34px; border-radius: 4px; background: var(--brand-red); opacity: 0.85; }

  .testimonial {
    position: absolute; left: 774px; top: 56px; width: 380px;
    font-style: italic; font-size: 13.2px; line-height: 17.6px; color: var(--ink);
  }
  .testimonial cite { font-style: normal; font-size: 10px; }
  .quote-mark {
    position: absolute; font-family: Georgia, serif; font-size: 52px; line-height: 1;
    color: #d9534f; font-weight: 700;
  }
  .quote-mark--open { left: 742px; top: 34px; }
  .quote-mark--close { left: 1128px; top: 106px; }
</style>
</head>
<body>

<section class="page page--left">
  <div class="section-label">COMMUNICATIONS</div>
  <h1 class="section-title">Keeping in touch with your team and customers at the office or on the road</h1>

  <div class="feature-icon" style="left:63px; top:240px;">
    <svg viewBox="0 0 24 24" aria-hidden="true"><path d="M10.6 13.4a1 1 0 0 1 0-1.4l3.5-3.5a1 1 0 1 1 1.4 1.4L12 13.4a1 1 0 0 1-1.4 0zM6.3 20.1a4.3 4.3 0 0 1-3-7.3l2.9-2.9a4.3 4.3 0 0 1 6 0 1 1 0 0 1-1.4 1.4 2.3 2.3 0 0 0-3.2 0l-2.9 2.9a2.3 2.3 0 0 0 3.2 3.2l1.2-1.2a1 1 0 0 1 1.4 1.4l-1.2 1.2a4.3 4.3 0 0 1-3 1.3zM14.7 14.1a4.3 4.3 0 0 1-3-1.3 1 1 0 0 1 1.4-1.4 2.3 2.3 0 0 0 3.2 0l2.9-2.9a2.3 2.3 0 0 0-3.2-3.2l-1.2 1.2a1 1 0 0 1-1.4-1.4l1.2-1.2a4.3 4.3 0 0 1 6 6l-2.9 2.9a4.3 4.3 0 0 1-3 1.3z"/></svg>
  </div>
  <div class="feature" style="left:174px; top:248px; width:360px;">
    <h2>NETWORK</h2>
    <p>Having a fast, reliable and secure business network is extremely important to be competitive and ensure your IT can operate.</p>
    <p>Voltrane offers a range of network services and support options such as:</p>
    <ul>
      <li>Network Services</li>
      <li>Network consulting</li>
      <li>Managed networks</li>
      <li>Private IP networks</li>
      <li>Remote Access</li>
      <li>Virtual private Networks</li>
    </ul>
  </div>

  <div class="feature-icon" style="left:63px; top:486px;">
    <svg viewBox="0 0 24 24" aria-hidden="true"><circle cx="12" cy="6.5" r="3"/><circle cx="5.5" cy="8.5" r="2.4"/><circle cx="18.5" cy="8.5" r="2.4"/><path d="M7 18c0-3.3 2.2-6 5-6s5 2.7 5 6z"/><path d="M1.5 17c0-2.6 1.7-4.7 4-4.7 1 0 1.8.3 2.4.9-.9 1.1-1.4 2.4-1.5 3.8z"/><path d="M22.5 17c0-2.6-1.7-4.7-4-4.7-1 0-1.8.3-2.4.9.9 1.1 1.4 2.4 1.5 3.8z"/></svg>
  </div>
  <div class="feature" style="left:174px; top:491px; width:365px;">
    <h2>EMAIL COLLABORATION</h2>
    <p>Email is the way we communicate to our team and customers, but not all email services are the same or provide the same benefits.</p>
    <p>Security, spam and access on mobile devices is where we can help your business.</p>
    <p>Voltrane offers Cloudsuite Apps a leading email and collaboration suite that improve productivity while allowing access to your email, calendars and messages while in or out of the office.</p>
  </div>

  <div class="app-panel">
    <div class="app"><span class="app-mark"></span>Postbox</div>
    <div class="app"><span class="app-mark"></span>Filedock</div>
    <div class="app"><span class="app-mark"></span>Datebook</div>
    <div class="app"><span class="app-mark"></span>Cardfile</div>
    <div class="app"><span class="app-mark"></span>Chatline</div>
  </div>
</section>

<section class="page page--right">
</section>

<span class="quote-mark quote-mark--open">&ldquo;</span>
<blockquote class="testimonial">
  Facestion platus voluptam iur autem fuga. Ossit vollabor sima enem. Erorepu dandigeni aute nonet officil illaborem eos et aut et vent porum asita porendia nem hillia illo illique niet, tem que re, sequi consed quatis aliquatur. <cite>– Mia Harlow, BRIGHTKEY</cite>
</blockquote>
<span class="quote-mark quote-mark--close">&rdquo;</span>

<div class="feature-icon" style="left:663px; top:240px;">
  <svg viewBox="0 0 24 24" aria-hidden="true"><path d="M6.6 10.8a15.1 15.1 0 0 0 6.6 6.6l2.2-2.2a1 1 0 0 1 1-.25 11.4 11.4 0 0 0 3.6.57 1 1 0 0 1 1 1V20a1 1 0 0 1-1 1A17 17 0 0 1 3 4a1 1 0 0 1 1-1h3.5a1 1 0 0 1 1 1c0 1.25.2 2.45.57 3.57a1 1 0 0 1-.25 1z"/></svg>
</div>
<div class="feature feature--spaced" style="left:774px; top:248px; width:365px;">
  <h2>OFFICE PHONES</h2>
  <p>With your internet service you can have office phones that can call local, national and mobiles at heavily discounted rates.</p>
  <p>Using the internet offers many great phone features such as message to email. Attended call transferring and out of hours messages when calling outside your normal trading hours.</p>
  <p>With a push of a button on your office phone you can divert all calls to your mobile, receptionist or team member.</p>
  <p>Voltrane’s digital office phones are an appropriate solution where:</p>
  <ul>
    <li>Your business is geographically dispersed but wishes to appear as one unified organisation with central or multiple call management/monitoring points.</li>
    <li>Your business wishes to use IP telephony without significant investment in hardware, software and technical support.</li>
    <li>You require a flexible phone system that provides staff with the ability to relocate quickly and seamlessly between offices, home, interstate and overseas without disruption.</li>
  </ul>
</div>

</body>
</html>
```